Sagebrush Hollow CBD Apothecary needs label for CBD capsule bottles

I need a 1 1/2"H x 3.5" W label for a cobalt blue glass pill bottle. Looking for apothecary look, but not over the top. I would like a yellow background (ccff00), or combination thereof, and my company logo/name, in addition to the text "PURE CBD CRYSTAL ISOLATE", Dietary Supplement, Ingredients: 99.1% Cannabidiol Crystal Isolate, Lab Tested, ZERO THC, NO FILLERS, Keep Out of Reach of Children, Serving Suggestion: Take one Plantulet Daily, increase dosage as needed, Storage- cool dry place away from light and heat, www.shcbdstore.example

Target Market(s)

Adults with health issues, all ages.

Industry/Entity Type

Health And Wellness

Other font styles liked:
• similar to Algerian. Apothecary fonts.

Colors
fbee3d

Requirements
Must have
• Logo and Company name, "SAGEBRUSH HOLLOW CBD APOTHECARY"
• Yellow to contrast cobalt blue bottles
Nice to have
• Made in Pinon Wash, CA.
• Vegan Capsules
• NO GMO
Should not have
• no pot leaves or anything overtly cannabis related. No script fonts.

```html
<!DOCTYPE html>
<html lang="en">
<head>
<meta charset="utf-8">
<title>Sagebrush Hollow CBD Apothecary – Pure CBD Crystal Isolate Label</title>
<link rel="stylesheet" href="https://fonts.googleapis.com/css2?family=Cinzel+Decorative:wght@700;900&family=Open+Sans:wght@400;600;700&display=swap">
<style>
  :root {
    --label-yellow: #f5ee3f;
    --ink: #231f20;
    --ornament-tone: #e0d634;
    --page: #ffffff;
  }
  * { box-sizing: border-box; margin: 0; padding: 0; }
  html, body { width: 1200px; height: 1200px; overflow: hidden; background: var(--page); }
  .canvas { position: relative; width: 1200px; height: 1200px; color: var(--ink); font-family: "Open Sans", Arial, sans-serif; }
  .label-shape { position: absolute; inset: 0; width: 1200px; height: 1200px; }

  .brand { position: absolute; left: 330px; top: 410px; width: 196px; text-align: center; }
  .brand-mark { width: 120px; height: 120px; margin: 0 auto 26px; border: 3px solid var(--ink); border-radius: 50%; }
  .brand-name { font-family: "Cinzel Decorative", Georgia, serif; font-weight: 700; font-size: 14px; line-height: 1.15; letter-spacing: 0.2px; }

  .product-title { position: absolute; left: 536px; top: 416px; font-family: "Cinzel Decorative", Georgia, serif; font-weight: 900; font-size: 64px; line-height: 71px; letter-spacing: 1px; }

  .ornament { position: absolute; top: 440px; width: 116px; height: 46px; background: var(--ornament-tone); border-radius: 23px; }
  .ornament-left { left: 180px; }
  .ornament-right { left: 924px; }

  .category { position: absolute; left: 0; width: 1220px; top: 641px; text-align: center; font-weight: 600; font-size: 20px; }

  .info-table { position: absolute; left: 192px; top: 670px; width: 834px; height: 97px; display: grid; grid-template-columns: 187px 446px 201px; border: 1px solid var(--ink); }
  .info-cell { padding-top: 12px; text-align: center; font-size: 13.5px; line-height: 15.5px; }
  .info-cell + .info-cell { border-left: 1px solid var(--ink); }
  .info-heading { font-weight: 600; font-size: 14px; }
  .info-origin { margin-top: 22px; font-weight: 600; font-size: 15.5px; }

  .website { position: absolute; left: 0; width: 1220px; top: 777px; text-align: center; font-weight: 700; font-size: 13px; }
</style>
</head>
<body>
<main class="canvas">
  <svg class="label-shape" viewBox="0 0 1500 1500" aria-hidden="true">
    <path fill="var(--label-yellow)" stroke="var(--ink)" stroke-width="6" stroke-linejoin="round"
      d="M178,525 L275,525 C290,505 300,492 320,490 C450,485 650,470 730,478 C750,480 760,488 763,492 C766,488 776,480 796,478 C876,470 1076,485 1206,490 C1226,492 1236,505 1251,525 L1348,525 L1348,683 C1300,700 1295,730 1295,749 C1295,770 1300,800 1348,815 L1348,972 L1251,972 C1236,992 1226,1005 1206,1007 C1076,1012 876,1010 790,1012 C776,1014 768,1020 763,1025 C758,1020 750,1014 736,1012 C650,1010 450,1012 320,1007 C300,1005 290,992 275,972 L178,972 L178,815 C226,800 232,770 232,749 C232,730 226,700 178,683 Z"/>
  </svg>

  <div class="ornament ornament-left" role="img" aria-label="Decorative scroll flourish"></div>
  <div class="ornament ornament-right" role="img" aria-label="Decorative scroll flourish"></div>

  <div class="brand">
    <div class="brand-mark"></div>
    <p class="brand-name">SAGEBRUSH HOLLOW CBD<br>APOTHECARY</p>
  </div>

  <h1 class="product-title">PURE CBD<br>CRYSTAL<br>ISOLATE</h1>

  <p class="category">Dietary Supplement</p>

  <section class="info-table">
    <div class="info-cell">
      <p class="info-heading">Ingredients</p>
      <p>99.1% Cannabidiol<br>Crystal Isolate,<br>Lab Tested, Zero<br>THC, No Fillers</p>
    </div>
    <div class="info-cell">
      <p class="info-heading">Storage</p>
      <p>Cool Dry place away from Light and Heat</p>
      <p class="info-origin">Made in Pinon Wash, CA. &nbsp;- &nbsp;Vegan Capsules &nbsp;- &nbsp;No GMO</p>
    </div>
    <div class="info-cell">
      <p class="info-heading">Serving Suggestion</p>
      <p>Take one Plantulet<br>Daily, increase dosage<br>as needed</p>
    </div>
  </section>

  <p class="website">www.shcbdstore.example</p>
</main>
</body>
</html>
```